Business Card Design Project

This is a new division in our company. "Meridale Wellsite & Safety" This is a Oilfield Safety company. I have included our new logo. I also have given our other business card. We love double sided with lots of color. We like to stand out. Please DO NOT duplicate our other card and bring your design into it. See all attached files.
Reason: forgot to change this when I posted it.
Here is the correct information card.
www.meridalewellsitesafety.com
Dwayne@meridalewellsitesafety.com
Reason: revision for a few.
Reason: was traveling and need to review designs.
Oil and Gas industry. Masculine look.
Business

```html
<!DOCTYPE html>
<html lang="en">
<head>
<meta charset="utf-8">
<title>Meridale Wellsite &amp; Safety – Business Card</title>
<link rel="stylesheet" href="https://fonts.googleapis.com/css2?family=Michroma&family=Orbitron:wght@700&display=swap">
<style>
  :root {
    --bg: #c9c9c9;
    --black: #0b0b0b;
    --charcoal: #2a2a2a;
    --white: #f4f4f2;
    --teal: #2fb3b0;
    --orange: #e8542a;
    --green: #3aa94a;
    --sky: #27b2c4;
    --red: #e0222a;
    --amber: #f0a032;
    --lime: #c8d82c;
    --ink: #1c1c1c;
    --card-w: 760px;
    --card-h: 434px;
  }
  * { box-sizing: border-box; margin: 0; padding: 0; }
  html, body { width: 1200px; height: 1000px; overflow: hidden; }
  body {
    background: linear-gradient(180deg, #e6e6e6 0%, var(--bg) 100%);
    font-family: "Michroma", sans-serif;
    display: flex; flex-direction: column; align-items: center; justify-content: center; gap: 40px;
  }
  .card {
    position: relative; width: var(--card-w); height: var(--card-h);
    overflow: hidden; box-shadow: 0 10px 30px rgba(0,0,0,.3);
  }
  .card svg.shapes { position: absolute; inset: 0; }
  .wordmark {
    position: absolute; display: flex; align-items: center; gap: 12px;
    color: var(--teal); font-size: 22px; letter-spacing: 1px; line-height: 1.25;
  }
  .wordmark .mark { width: 18px; height: 18px; background: var(--teal); flex: none; }
  /* front */
  .card--front { background: var(--black); }
  .card--front .wordmark { left: 150px; top: 180px; font-size: 26px; }
  /* back */
  .card--back { background: var(--white); }
  .card--back .wordmark { left: 34px; top: 52px; font-size: 17px; }
  .contact-lines {
    position: absolute; left: 470px; top: 50px;
    font-size: 14px; line-height: 1.75; color: var(--ink);
  }
  .person { position: absolute; right: 30px; top: 166px; text-align: right; }
  .person-name { font-family: "Orbitron", sans-serif; font-weight: 700; font-size: 26px; color: var(--teal); letter-spacing: 1px; }
  .person-email { font-size: 12px; color: #d8d8d8; margin-top: 6px; }
  .address-lines {
    position: absolute; left: 200px; top: 318px;
    font-size: 14px; line-height: 1.8; color: var(--ink);
  }
</style>
</head>
<body>

<section class="card card--front" aria-label="Card front">
  <svg class="shapes" width="760" height="434" viewBox="0 0 760 434">
    <polygon points="600,0 760,0 760,434 440,434 740,205" fill="var(--charcoal)"/>
    <polyline points="600,0 740,205 440,434" fill="none" stroke="var(--sky)" stroke-width="7"/>
    <polyline points="588,0 728,205 428,434" fill="none" stroke="var(--green)" stroke-width="7"/>
    <polyline points="576,0 716,205 416,434" fill="none" stroke="var(--orange)" stroke-width="7"/>
  </svg>
  <div class="wordmark"><span class="mark"></span><span>MERIDALE<br>WELLSITE &amp; SAFETY</span></div>
</section>

<section class="card card--back" aria-label="Card back">
  <svg class="shapes" width="760" height="434" viewBox="0 0 760 434">
    <defs>
      <linearGradient id="band" x1="0" y1="0" x2="0" y2="1">
        <stop offset="0" stop-color="#3a3a3a"/>
        <stop offset=".5" stop-color="#111"/>
        <stop offset="1" stop-color="#000"/>
      </linearGradient>
    </defs>
    <polygon points="0,0 420,0 320,150 0,150" fill="var(--charcoal)"/>
    <rect x="0" y="150" width="760" height="82" fill="url(#band)"/>
    <polygon points="0,232 260,232 150,300 0,300" fill="var(--charcoal)"/>
    <line x1="700" y1="0" x2="760" y2="80" stroke="var(--lime)" stroke-width="6"/>
    <polygon points="760,268 760,434 520,434" fill="var(--amber)"/>
    <polygon points="735,268 760,268 520,434 490,434" fill="var(--red)"/>
  </svg>
  <div class="wordmark"><span class="mark"></span><span>MERIDALE<br>WELLSITE &amp; SAFETY</span></div>
  <div class="contact-lines">
    <p>Fax: 1-888-555-0147</p>
    <p>Office: 201 - 555 0183</p>
    <p>Cell: 713-555-0126</p>
  </div>
  <div class="person">
    <p class="person-name">Dwayne Halvorsen</p>
    <p class="person-email">Email: Dwayne@meridalewellsitesafety.com</p>
  </div>
  <div class="address-lines">
    <p>4810 N. Ridgeline, TX 77301</p>
    <p>www.MeridaleWellsiteSafety.com</p>
  </div>
</section>

</body>
</html>
```